依頼詳細
今回は、トップページデザインの募集になります。
レスポンシブデザインのサイトで、bootstrap4を利用しコーディングする予定になります。
デザイン幅は2000px、コンテンツの幅はbootstrap4デフォルトの1110pxを基準としてください。ただし最近のデザインの流行を取りいれて、フルワイドや、1200~15000px程度の幅のコンテンツをバランスよくレイアウトしてください。
コンテンツ配置は基本12分割になります。がデザインによっては、多少逸脱してもかまいません。
念のため、サンプルのPSDデータを添付しますので、参照ください。

本文のフォントはゴシック系は游ゴシック、メイリオ、明朝系は遊明朝でお願いします。
飾り文字はフリーフォントか、googleフォントを利用してください。

メイン画像部分・グローバルメニューは、ワイド適用でお願いします。

資料上はサイト名(社名)や住所などは伏字にしております。ご提案時点ではそのまま作成をお願いします。当選確定後、本内容に修正をお願いいたします。

当選の方は、希望があれば引き続き下層ページの作成及びコーディング作業を依頼可能です。
不明点、質問などありましたらメッセージ等でご連絡ください。

・カラー
青系(爽やかなイメージ)

・掲載画像
必ず添付ファイルを使用してください。
また、雰囲気が合っていれば、指定外の画像を背景などに使用いただいてもOKです。

・その他
内容詳細に関しては、別添のExcel資料を参照してください。
ページ数
1ページ
希望イメージ
シンプル 複雑
単色 カラフル
暗い 明るい
日常 高級
遊び心 厳粛
未来的 伝統的
女性的 男性的
希望する色
青系、水色系
納品ファイル
• 高解像度JPG (.jpg)
• フォトショップ形式 (.psd)
補足説明
納品ファイルは、PDF及びクライアント表示確認用のJPGを準備お願いします。
■ 選んだ理由

今回は、贅沢さや豪華さをイメージさせる洗練された先進的なデザインを希望しており、見た目が大事な案件でした。
業界的に国内外問わず「サイトの見た目」をかなり重要視しているため、"見栄えのするデザイン"というところに重きを置いてクライアントとの折衝の結果、skytrailふじさわ様を選定させていただきました。

■ 提案者全員のお礼・コメント

どの案も制作意図を組んでいただきとてもよかったのですが、今回はskytrailふじさわ様を当選とさせていただきました。
皆様ご提案ありがとうございました。
今後ともご提案宜しくお願いいたします。

```html
<!DOCTYPE html>
<html lang="ja">
<head>
<meta charset="utf-8">
<title>○○○○○○○○株式会社 | Safety High Quality</title>
<link rel="stylesheet" href="https://fonts.googleapis.com/css2?family=Noto+Sans+JP:wght@300;400;500;700&family=Raleway:wght@300;400;500&display=swap">
<style>
:root{
  --blue:#2b7fd0;
  --blue-deep:#1f4f8e;
  --navy:#2a3f63;
  --sky:#8cc7ef;
  --pale:#eef3fa;
  --pale-2:#e3ebf5;
  --line:#c9d5e4;
  --text:#333b47;
  --muted:#6c7888;
  --white:#ffffff;
}
*{margin:0;padding:0;box-sizing:border-box}
html,body{width:1200px;height:2800px;overflow:hidden}
body{font-family:"Noto Sans JP",sans-serif;color:var(--text);background:var(--white);position:relative}
.en{font-family:"Raleway",sans-serif;font-weight:300;letter-spacing:.06em}
.ph{position:absolute;display:block}
.btn{position:absolute;display:flex;align-items:center;justify-content:center;gap:10px;width:150px;height:30px;border:1px solid var(--blue);border-radius:15px;font-family:"Raleway",sans-serif;font-size:11px;letter-spacing:.12em;color:var(--blue);background:var(--white)}
.btn::after{content:"";width:18px;height:1px;background:var(--blue)}

/* hero */
.hero{position:absolute;left:0;top:0;width:1200px;height:440px;overflow:hidden}
.hero .ph{inset:0;background:linear-gradient(180deg,#3d8fd6 0%,#7fc0ee 35%,#cfe6f6 58%,#5aa7d8 72%,#1f78bf 100%)}
.hero .curve{position:absolute;left:0;bottom:0;width:1200px;height:90px}
.gnav{position:absolute;right:60px;top:14px;display:flex;gap:0}
.gnav a{display:block;width:82px;text-align:center;color:var(--white);text-decoration:none;border-left:1px solid rgba(255,255,255,.5)}
.gnav a:first-child{border-left:none}
.gnav .en{display:block;font-size:12px;font-weight:500}
.gnav .ja{display:block;font-size:9px;margin-top:2px}
.hero-copy{position:absolute;left:700px;top:175px;color:var(--white);text-align:right;width:350px}
.hero-copy .l1{font-size:50px;line-height:1.1;padding-right:40px}
.hero-copy .l2{font-size:56px;line-height:1.1}
.hero-copy .sub{font-size:11px;letter-spacing:.3em;margin-top:8px}

/* intro */
.intro{position:absolute;left:0;top:495px;width:1200px;text-align:center}
.intro h1{font-size:26px;font-weight:700;letter-spacing:.06em}
.intro p{font-size:13px;line-height:2;margin-top:22px;color:var(--text)}

/* feature blocks */
.panel{position:absolute;background:var(--pale)}
.feature-title{position:absolute;display:flex;align-items:baseline;gap:12px}
.feature-title .en{font-size:11px;color:var(--muted);letter-spacing:.2em}
.feature-title .ja{font-size:18px;font-weight:500;color:var(--blue-deep)}
.feature-text{position:absolute;font-size:11px;line-height:1.9;color:var(--muted);width:220px}

/* bus */
.bus-band{position:absolute;left:0;top:1340px;width:1200px;height:260px;background:var(--pale-2)}
.bus-photo{left:270px;top:1340px;width:660px;height:260px;border-radius:0 0 0 0;background:linear-gradient(180deg,#4b97dd 0%,#9ccbee 45%,#d8dfe6 70%,#9aa4ad 100%)}
.circle-title{position:absolute;width:180px;height:180px;border-radius:50%;background:var(--white);text-align:center;padding-top:40px}
.circle-title .en{display:block;font-size:28px;color:var(--blue)}
.circle-title .ja{display:block;font-size:11px;margin-top:4px;color:var(--muted)}

/* info */
.info-head{position:absolute;left:270px;top:1680px}
.info-head .en{display:block;font-size:30px;color:var(--blue)}
.info-head .ja{display:block;font-size:11px;color:var(--muted);margin-top:4px}
.info-list{position:absolute;left:480px;top:1690px;width:450px;list-style:none;border-top:1px solid var(--line)}
.info-list li{display:flex;gap:36px;padding:13px 8px;border-bottom:1px solid var(--line);font-size:12px}
.info-list time{color:var(--blue);font-family:"Raleway",sans-serif}

/* contact */
.contact{position:absolute;left:0;top:1848px;width:1200px;height:272px}
.contact .ph{inset:0;background:linear-gradient(180deg,#34507a 0%,#4a6b99 50%,#2d4368 100%)}
.contact .veil{position:absolute;inset:0;background:rgba(35,65,110,.35)}
.contact-tel{position:absolute;left:490px;top:130px;color:var(--white);font-family:"Raleway",sans-serif;font-size:24px;line-height:1.35;letter-spacing:.08em}
.contact .btn{left:525px;top:218px;border-color:var(--white);color:var(--blue)}

/* footer */
.footer{position:absolute;left:0;top:2120px;width:1200px;height:680px;background:var(--white)}
.footer .ph{left:0;top:140px;width:1200px;height:540px;background:linear-gradient(180deg,#6fb4ec 0%,#a9d5f3 40%,#8a9bb0 75%,#4a5568 100%)}
.footer-info{position:absolute;left:248px;top:56px;background:rgba(255,255,255,.92);padding:12px 0}
.footer-name{font-size:22px;font-weight:500;letter-spacing:.1em;color:var(--navy)}
.footer-addr{font-size:10px;line-height:1.8;color:var(--muted);margin-top:8px}
.footer-nav{position:absolute;left:560px;top:56px;display:flex;gap:0}
.footer-nav a{display:block;width:84px;text-align:center;text-decoration:none;color:var(--text);border-left:1px solid var(--line)}
.footer-nav a:first-child{border-left:none}
.footer-nav .en{display:block;font-size:11px;font-weight:500}
.footer-nav .ja{display:block;font-size:9px;color:var(--muted);margin-top:2px}
.copyright{position:absolute;left:0;bottom:0;width:1200px;height:36px;line-height:36px;text-align:center;font-size:10px;color:var(--white);background:rgba(31,79,142,.8)}
</style>
</head>
<body>

<header class="hero">
  <div class="ph" role="img" aria-label="海沿いのリゾート都市と青い空の写真"></div>
  <nav class="gnav">
    <a href="#"><span class="en">HOME</span><span class="ja">ホーム</span></a>
    <a href="#"><span class="en">COMPANY</span><span class="ja">会社概要</span></a>
    <a href="#"><span class="en">BUS</span><span class="ja">車両紹介</span></a>
    <a href="#"><span class="en">SAFETY</span><span class="ja">安全方針</span></a>
    <a href="#"><span class="en">CONTACT</span><span class="ja">お問い合わせ</span></a>
  </nav>
  <div class="hero-copy en">
    <div class="l1">Safety</div>
    <div class="l2">High Quality</div>
    <div class="sub">○○○○○○ COMPANY</div>
  </div>
  <svg class="curve" viewBox="0 0 1200 90" preserveAspectRatio="none" aria-hidden="true">
    <path d="M0 20 C 300 95, 800 95, 1200 10 L1200 90 L0 90 Z" fill="#ffffff"/>
  </svg>
</header>

<section class="intro">
  <h1>より一層安全・安心なお客様サービスの実現へ</h1>
  <p>○○○○は、“Safety” と “High Quality” をモットーとし、<br>これからも“確かな安全・安心”と“最高水準のサービス”で地域と共に歩み続けます。</p>
</section>

<section class="company">
  <div class="panel" style="left:272px;top:732px;width:380px;height:228px"></div>
  <div class="ph" role="img" aria-label="高層ビルが並ぶ都市と緑の公園の写真" style="left:600px;top:660px;width:600px;height:272px;border-radius:40px 0 0 0;background:linear-gradient(180deg,#5da6e2 0%,#a8d2f0 45%,#8fa7b8 70%,#6d9a6a 100%)"></div>
  <div class="feature-title" style="left:300px;top:795px"><span class="en">COMPANY</span><span class="ja">会社概要</span></div>
  <p class="feature-text" style="left:300px;top:838px">創業以来培ってきた経験と信頼を大切に、地域の皆様の移動を支えています。</p>
  <a class="btn" href="#" style="left:300px;top:895px">VIEW MORE</a>
</section>

<section class="safety">
  <div class="panel" style="left:560px;top:990px;width:372px;height:230px"></div>
  <div class="ph" role="img" aria-label="港と山並みが見える街並みと青空の写真" style="left:0;top:960px;width:620px;height:340px;border-radius:0 40px 0 0;background:linear-gradient(180deg,#2f7fd0 0%,#8cc4ef 40%,#e2eef8 58%,#7d97ad 80%,#4d6a85 100%)"></div>
  <div class="feature-title" style="left:660px;top:1048px"><span class="en">SAFETY</span><span class="ja">安全方針について</span></div>
  <p class="feature-text" style="left:660px;top:1090px">安全を最優先に日々の点検と教育を徹底し、安心の運行を実現しています。</p>
  <a class="btn" href="#" style="left:740px;top:1135px">VIEW MORE</a>
</section>

<section class="bus">
  <div class="bus-band"></div>
  <div class="ph bus-photo" role="img" aria-label="駐車場に並ぶ大型観光バスの写真"></div>
  <div class="circle-title" style="left:510px;top:1320px;width:180px;height:130px;border-radius:0 0 90px 90px;padding-top:28px"><span class="en">BUS</span><span class="ja">車両のご紹介</span></div>
</section>

<section class="info">
  <div class="info-head"><span class="en">INFORMATION</span><span class="ja">お知らせ</span></div>
  <a class="btn" href="#" style="left:270px;top:1745px">VIEW MORE</a>
  <ul class="info-list">
    <li><time>2020.00.00</time><span>テキストテキストテキストテキスト</span></li>
    <li><time>2020.00.00</time><span>テキストテキスト</span></li>
  </ul>
</section>

<section class="contact">
  <div class="ph" role="img" aria-label="高層ビル街と走るバスの写真"></div>
  <div class="veil"></div>
  <div class="circle-title" style="left:510px;top:-30px;width:180px;height:130px;border-radius:0 0 90px 90px;padding-top:40px"><span class="en">CONTACT</span><span class="ja">お問い合わせ</span></div>
  <div class="contact-tel">TEL. 012-345-6789<br>FAX. 098-765-4321</div>
  <a class="btn" href="#">CONTACT</a>
</section>

<footer class="footer">
  <div class="ph" role="img" aria-label="夕暮れの繁華街と高層ビル群の写真"></div>
  <div class="footer-info">
    <div class="footer-name">○○○○○○○○株式会社</div>
    <p class="footer-addr">〒000-0000 ○○県○○市○○町0-0<br>TEL. 012-345-6789<br>FAX. 098-765-4321</p>
  </div>
  <nav class="footer-nav">
    <a href="#"><span class="en">HOME</span><span class="ja">ホーム</span></a>
    <a href="#"><span class="en">COMPANY</span><span class="ja">会社概要</span></a>
    <a href="#"><span class="en">BUS</span><span class="ja">車両紹介</span></a>
    <a href="#"><span class="en">SAFETY</span><span class="ja">安全方針</span></a>
    <a href="#"><span class="en">CONTACT</span><span class="ja">お問い合わせ</span></a>
  </nav>
  <div class="copyright">© ○○○○○○○○ Co., Ltd. All Rights Reserved.</div>
</footer>

</body>
</html>
```